Coded Website Design

I am opening a sustainable home consulting business. The core service areas will be lawn maintenance, sustainable landscape maintenance, Composting, Vermiculture, and Rain Harvesting. We will be designing sustainability programs metrics for the home owners and their families to demonstrate cost savings and the environmental impact of their efforts. We will use clean fueled equipment with a heavy emphasis electric powered equipment energized by solar powered chargers.

The purpose of the site:
Provide information on the company and services to potential customers.
Allow for customers to log in and schedule services, ask questions, pay bills and buy products.
Have a green living section with tips and resource's.
I will have a Chatterbox Page, Pipster, account Nuvola Ring, and a Quillstack blog set up in the company name. I would like the web presents and social
media have the same theme, common vocabulary and navigation.

The address for the site will be: bramwickyardco.example
Updates

Hi Everyone. The project has been temporarily closed since the client will be posting a logo design project. It will be reopened after the client has acquired a logo design, to be provided for this project.

Thanks,
QB Admin

Reason: I would like to give the designers additional time to submit proposals and allow myself adequate time to review and work with designers. While I am anxious to get the website design done and up for use, I do not want either the designers nor myself to feel that this is being rushed and unnecessarily compromise the design process due to a date constraint. I would like to get the best design and website I can and find the right designer to work with to accomplish this goal.

Thank you for those who have submitted a design.  I apologize for not having provided feedback to you, I was injured in an accident and have been unable to attend to work while I was recuperating.  I am going to extend the design period for an additional 7 days after which I will be back to work fulltime and work towards making a final selection.  I will be sending feedback to the designs previously submitted over the next few days.  Thank you again to the designers who have submitted designs, your patients and understanding.  

Reason: Thank you for those who have submitted a design. I apologize for not having provided feedback to you, I was injured in an accident and have been unable to attend to work while I was recuperating. I am going to extend the design period for an additional 7 days after which I will be back to work fulltime and work towards making a final selection. I will be sending feedback to the designs previously submitted over the next few days. Thank you again to the designers who have submitted designs, your patients and understanding.

Target Market(s)

Charlotte North Carolina Familys with an intgerest in sustainability and green living

Industry/Entity Type

Sustainability

Requirements
Must have
• I like techno sites that are not imposing and or intimidating, and that utilize technology in a way that makes the experience memorable.

I like sites that are easy and intuitive to navigate.

I like the home page to tell a story using sound, voice, graphics, pictures to guide the customer to the next page. I don't like looking at a borage of text blocks .

it needs to be able to schedule appointments and services, purchase merchandise, pay bills, offer feedback

the blog, website and if possible app should be an extension of each other and be easy to go from one to the other
Nice to have
• easy navigation, be fun, teach something new, tell a story, be memorable

I like pages that utilize flash.
I really like http://plumtreeworks.example/examples.php
Should not have
• I don't like sites that are a series of text blocks that look like the yellow pages.

I don't like navigation that is circular in nature

redundancy is not good unless necessary

```html
<!DOCTYPE html>
<html lang="en">
<head>
<meta charset="utf-8">
<title>Bramwick Yard Co</title>
<link rel="stylesheet" href="https://fonts.googleapis.com/css2?family=Cinzel:wght@400;600&family=Arimo:wght@400;700&display=swap">
<style>
:root{
  --green:#8cc63f;
  --green-deep:#7db92f;
  --white:#ffffff;
  --frame:#ececec;
  --ink:#2b2b2b;
  --text:#333333;
  --muted:#6a6a6a;
  --blue:#12a6d6;
  --dark:#2a2a2a;
  --accent-nav:#1aa3cf;
}
*{box-sizing:border-box;margin:0;padding:0}
html,body{width:1200px;height:932px;overflow:hidden}
body{position:relative;background:linear-gradient(var(--green),var(--green-deep));font-family:Arimo,Arial,sans-serif;color:var(--text)}
.top-band{position:absolute;left:0;top:0;width:1200px;height:190px;background:linear-gradient(#f2f2f2,#ffffff 60px)}
.brand{position:absolute;left:113px;top:38px;display:flex;flex-direction:column;align-items:flex-start;gap:14px}
.brand-dot{width:48px;height:48px;border-radius:50%;background:var(--green);margin-left:56px}
.brand-name{font-family:Cinzel,serif;font-size:22px;color:#555;letter-spacing:.5px;white-space:nowrap}
.social{position:absolute;top:16px;right:103px;display:flex;gap:8px;list-style:none}
.social li{width:33px;height:33px;border-radius:50%;display:flex;align-items:center;justify-content:center}
.social .chatterbox{background:#1d4f7a}
.social .pipster{background:#1aa9e1}
.social .feed{background:#f39200}
.social .mail{background:#b3b3b3}
.main-nav{position:absolute;top:100px;right:106px;display:flex;gap:46px;list-style:none;font-family:Cinzel,serif;font-size:17px;color:var(--ink)}
.main-nav li{padding-bottom:6px}
.main-nav .current{border-bottom:2px solid var(--accent-nav)}
.slider{position:absolute;left:102px;top:148px;width:996px;height:462px;background:var(--frame)}
.slide{position:absolute;left:5px;top:7px;width:985px;height:449px;background:linear-gradient(#7fb2e0 0%,#cfe3f2 30%,#4f8f2c 55%,#3f7a1f 80%,#6d4a2a 100%)}
.slide-dots{position:absolute;right:6px;bottom:6px;width:107px;height:41px;background:rgba(30,30,30,.85);display:flex;align-items:center;justify-content:flex-end;gap:9px;padding-right:12px}
.slide-dots span{width:16px;height:16px;border-radius:50%;background:#d6d6d6}
.slide-dots .active{background:var(--blue)}
.arrow{position:absolute;top:360px}
.arrow.prev{left:42px}
.arrow.next{left:1126px}
.content{position:absolute;left:102px;top:610px;width:996px;height:265px;background:var(--white)}
.welcome{position:absolute;left:11px;top:22px;width:668px}
.welcome h1{font-family:Cinzel,serif;font-weight:600;font-size:25px;color:var(--ink);letter-spacing:.3px}
.welcome p{margin-top:12px;font-size:12.6px;line-height:20px;text-align:justify;padding-left:2px}
.read-more{display:inline-block;margin-top:12px;background:var(--blue);color:#fff;font-size:13px;padding:2px 6px;border-radius:3px;width:77px}
.video{position:absolute;left:694px;top:29px;width:295px;height:204px;background:var(--dark);padding:5px}
.video-still{width:285px;height:164px;background:linear-gradient(#3f8fd6,#a9d3ef 40%,#5aa83a 70%,#8ab48a);position:relative}
.play{position:absolute;left:111px;top:61px;width:62px;height:44px;background:rgba(40,40,40,.8);border-radius:4px}
.controls{height:26px;background:#e9e9e9;display:flex;align-items:center;gap:8px;padding:0 6px;font-size:10.5px;font-weight:700;color:#222}
.track{flex:1;height:5px;background:#888;border-radius:3px}
.site-footer{position:absolute;left:101px;top:875px;width:996px;height:42px;background:var(--dark);border-radius:0 0 6px 6px;color:#fff;font-size:12.5px;padding:14px 14px}
.chat-tab{position:absolute;left:830px;top:887px;width:252px;height:50px;background:var(--blue);border:2px solid #fff;border-radius:6px 6px 0 0;color:#fff;font-weight:700;font-size:15px;padding:12px 12px;display:flex;align-items:center;gap:10px}
</style>
</head>
<body>
<header class="top-band">
  <div class="brand">
    <span class="brand-dot"></span>
    <span class="brand-name">Bramwick Yard Co</span>
  </div>
  <ul class="social">
    <li class="chatterbox" aria-label="Chatterbox"></li>
    <li class="pipster" aria-label="Pipster"></li>
    <li class="feed" aria-label="Feed">
      <svg width="13" height="13" viewBox="0 0 13 13"><circle cx="2" cy="11" r="1.8" fill="#fff"/><path d="M1 5a7 7 0 0 1 7 7M1 1a11 11 0 0 1 11 11" stroke="#fff" stroke-width="2" fill="none"/></svg>
    </li>
    <li class="mail" aria-label="Email">
      <svg width="15" height="11" viewBox="0 0 15 11"><rect x="0.5" y="0.5" width="14" height="10" fill="#fff"/><path d="M1 1l6.5 5L14 1" stroke="#b3b3b3" fill="none"/></svg>
    </li>
  </ul>
  <ul class="main-nav">
    <li class="current">Home</li><li>Works</li><li>About</li><li>Features</li><li>News</li><li>Contacts</li>
  </ul>
</header>

<svg class="arrow prev" width="34" height="56" viewBox="0 0 34 56"><path d="M32 2L4 28l28 26" stroke="#fff" stroke-width="4" fill="none"/></svg>
<svg class="arrow next" width="34" height="56" viewBox="0 0 34 56"><path d="M2 2l28 26L2 54" stroke="#fff" stroke-width="4" fill="none"/></svg>

<section class="slider">
  <div class="slide" role="img" aria-label="Photo of a large round tree beside a fenced path through green tea fields under a blue sky"></div>
  <div class="slide-dots"><span></span><span class="active"></span><span></span><span></span></div>
</section>

<main class="content">
  <article class="welcome">
    <h1>Welcome to Bramwick Yard Co</h1>
    <p>simply dummy text of the printing and typesetting industry. Lorem Ipsum has been the industry's standard dummy text ever since the 1500s, when an unknown printer took a galley of type and scrambled it to make a type specimen book. It has survived not only five centuries, but also the leap into electronic typesetting, remaining essentially unchanged. It was popularised in the 1960s with the release of Glyphline sheets containing Lorem Ipsum passages, and more recently with desktop publishing software like Pressmark Layout including versions Ipsum is not simply random text. It has roots in a piece of classical Latin literature from 45 BC, making it over 2000 years old. Edmund Harrow, a Latin professor at Ashgrove College in Vermont,of Lorem Ipsum.</p>
    <span class="read-more">read more</span>
  </article>
  <div class="video">
    <div class="video-still" role="img" aria-label="Video still of a cottage garden with a paved path, a bench and a pond">
      <svg class="play" viewBox="0 0 62 44"><path d="M23 11l18 11-18 11z" fill="#fff"/></svg>
    </div>
    <div class="controls">
      <svg width="8" height="9" viewBox="0 0 8 9"><path d="M0 0l8 4.5L0 9z" fill="#222"/></svg>
      <span>00:00</span><span class="track"></span><span>00:00</span>
      <svg width="26" height="10" viewBox="0 0 26 10"><path d="M0 3h3l3-3v10L3 7H0z" fill="#333"/><path d="M9 9V7M12 9V6M15 9V5M18 9V3M21 9V2M24 9V1" stroke="#333"/></svg>
      <svg width="10" height="10" viewBox="0 0 10 10"><path d="M0 3V0h3M7 0h3v3M10 7v3H7M3 10H0V7" stroke="#333" fill="none"/></svg>
    </div>
  </div>
</main>

<footer class="site-footer">Copyright © 2013 BRAMWICK YARD CO, LLC. All rights reserved.</footer>

<div class="chat-tab">Offine- Leave a message
  <svg width="11" height="7" viewBox="0 0 11 7"><path d="M1 6l4.5-4.5L10 6" stroke="#fff" stroke-width="2" fill="none"/></svg>
</div>
</body>
</html>
```